Zielgruppe
Unsere Vorstellung währe eine Flyer Falzflyer DIN lang 6-seitig oder 4-seitig,
wir sind für alle Vorschläge offen.
Wir sind eine Umzugsfirma für Privatumzüge, Firmenumzüge und Personaldienstleistung und kümmern uns um alles was in einem Umzug anfällt bzw. verpacken der Möbel Auf und Abbau der Möbel, Einpackservice aller Haushaltsgegenstände, darüber hinaus stellen wir auch nur Umzugshelfer.
Montage von Neumöbel wie Wandbrook durch geschultes Personal.
Die Infos wie z.B E-Mail, und Telefon sollten auch auf das Produkt.
E-Mail : info@pkv-transporte.example
Tel. 0049 152 38847261
Adresse: Lerchenfeldweg 27
74395 Lindenau am Kocher
Der Tex sollte noch enthalten:
Über uns:
PKV Transporte ist ein erfahrenes und kompetentes Umzugsunternehmen aus Talbrunn.
Innerhalb der Umzugsbranche reduzieren wir uns nicht nur auf Privatumzüge, den unsere Palette reicht vom Firmenumzug, Entrümpelung und Ankauf von gebrauchte Büromöbeln so wie Personaldienstleistung in der Möbelbrache.
Wir bieten Ihnen:
-TOP Qualität zu fairen Preisen
-Wissen aus jahrelanger Erfahrung
-persönliche Beratung von der Idee bis zum Umzug
-ausgebildete Fachkräfte für Montagearbeiten, Entrümpelung, Ein- und Auspackservice das alles mit den Modernsten und besten Werkzeugen.
-Terminsicherheit auch bei kurzfristigem Umzugswunsch
-Einen verlässlichen Umzugspartner
Privatumzüge:
Sie freuen sich auf Ihre neuen vier Wände.
Vorher steht eine Menge Arbeit ins Haus: Ihr Umzug.
Kein Problem, wir packen das für Sie an.
PKV Transporte macht Ihren Möbeln Beine !
Unser Leistungsspektrum umfasst alle Dienstleistungen rund um Ihren Umzug aus einer Hand:
Wir packen ein und aus, demontieren und montieren sämtliche Möbel,
leisten fachgerechte Schreiner-, Elektro- und Installationsarbeiten.
Bei uns sind Sie auf der sicheren Seite !
Es wird alles zu einem Festpreis..
Aufgabenstellung
Wir möchten das der Text Modern, kurz und knackig ist , darf auch etwas aus der reihe tanzen

```html
<!DOCTYPE html>
<html lang="de">
<head>
<meta charset="utf-8">
<title>PKV Transporte – Falzflyer</title>
<link href="https://fonts.googleapis.com/css2?family=Montserrat:ital,wght@0,400;0,500;0,600;0,700;1,400;1,600&display=swap" rel="stylesheet">
<style>
:root{
  --navy:#56647f;
  --navy-dark:#4a5670;
  --orange:#ee7d22;
  --text:#5a5f69;
  --paper:#fbfbfb;
  --bg:#ececec;
}
*{box-sizing:border-box;margin:0;padding:0}
html,body{width:1200px;height:2455px;overflow:hidden;background:var(--bg);font-family:'Montserrat',sans-serif;color:var(--text)}
.spread{position:absolute;left:60px;width:1080px;height:766px;display:flex;box-shadow:0 10px 30px rgba(0,0,0,.12)}
.spread--inside{top:250px}
.spread--outside{top:1410px}
.panel{position:relative;width:360px;height:766px;background:var(--paper);overflow:hidden}
.panel + .panel{border-left:1px solid #e4e4e4}
.band-top{position:absolute;top:0;left:0;right:0;height:8px;background:var(--navy)}
.band-top--orange{background:var(--orange)}
.band-left{position:absolute;top:0;bottom:0;left:0;width:9px;background:var(--navy)}
.heading{font-weight:700;color:var(--navy);text-transform:uppercase;letter-spacing:.5px}
.rule{height:1px;background:var(--orange);margin:12px 0}

/* offers */
.offers{padding:40px 28px 0 38px}
.offers .heading{font-size:22px;border-bottom:2px solid var(--navy);padding-bottom:8px;margin-bottom:22px}
.offer{display:flex;gap:12px;padding-bottom:14px;margin-bottom:16px;border-bottom:1px solid var(--orange)}
.offer-icon{flex:none;width:30px;height:30px}
.offer-title{font-size:12px;font-weight:700;color:var(--orange);text-transform:uppercase}
.offer-text{font-size:12px;font-weight:600;color:var(--navy-dark);line-height:1.35}
.ticks{list-style:none;margin-top:6px}
.ticks li{display:flex;align-items:center;gap:6px;font-size:12px;font-weight:600;color:var(--navy-dark);margin-bottom:4px}
.ticks svg{width:11px;height:11px;flex:none}
.contact{position:absolute;left:38px;right:28px;bottom:34px;text-align:center}
.contact-label{font-size:12px;font-weight:700;color:var(--navy);text-transform:uppercase}
.contact-mail{font-size:14px;font-weight:700;color:var(--orange);margin-top:4px;border-bottom:1px solid var(--orange);padding-bottom:6px}

/* photo blocks */
.photo{position:absolute;left:0;right:0;top:0}
.photo-fill{position:absolute;inset:0}
.photo-curve{position:absolute;left:0;bottom:-1px;width:100%;height:90px}
.badge{position:absolute;width:96px;height:96px;border-radius:50%;background:var(--navy);border:5px solid #fff;box-shadow:0 0 0 2px var(--navy);color:#fff;text-align:center;padding-top:14px}
.badge svg{width:14px;height:14px}
.badge-label{font-size:7px;letter-spacing:2px;margin-top:1px}
.badge-number{font-size:12px;font-weight:700;line-height:1.1}

.copy{position:absolute;left:30px;right:30px}
.copy .heading{font-size:21px;line-height:1.1;margin-bottom:14px}
.copy p{font-size:11.5px;line-height:1.45;margin-bottom:10px}
.copy .lead{font-weight:700;color:var(--navy-dark);font-style:italic}
.copy .accent{font-weight:700;color:var(--orange);font-style:italic}
.copy .quiet{font-style:italic}

/* address panel */
.panel--navy{background:var(--navy);color:#fff;text-align:center}
.brand{font-weight:700;text-transform:uppercase;letter-spacing:1px}
.panel--navy .brand{margin-top:210px;font-size:28px}
.address-list{margin:60px 34px 0}
.address-item{border-top:1px solid rgba(255,255,255,.6);margin-bottom:28px}
.address-item svg{width:26px;height:26px;margin-top:-13px;background:var(--navy)}
.address-item p{font-size:13px;font-weight:600;line-height:1.4;margin-top:4px}
.web-caps{font-size:15px;font-weight:600;letter-spacing:1px;margin-top:20px}

/* cover */
.cover-brand{position:absolute;top:50px;left:0;right:0;text-align:center;font-size:30px;color:var(--navy)}
.cover-brand::after{content:"";display:block;width:160px;height:2px;background:var(--orange);margin:10px auto 0}
.cover-title{position:absolute;left:20px;right:20px;bottom:86px;text-align:center;font-size:25px;line-height:1.1;white-space:nowrap}
.cover-web{position:absolute;left:30px;right:30px;bottom:40px;text-align:center;font-size:14px;font-weight:700;color:var(--orange);border-top:1px solid var(--orange);padding-top:6px}
</style>
</head>
<body>

<section class="spread spread--inside">
  <article class="panel">
    <div class="band-left"></div>
    <div class="offers">
      <h2 class="heading">Wir bieten Ihnen</h2>

      <div class="offer">
        <svg class="offer-icon" viewBox="0 0 30 30"><circle cx="15" cy="15" r="14" fill="none" stroke="#ee7d22" stroke-width="2"/><path d="M9 15l4 4 8-8" fill="none" stroke="#56647f" stroke-width="2.5"/></svg>
        <div><div class="offer-title">TOP Qualität</div><div class="offer-text">zu fairen Preisen.</div></div>
      </div>
      <div class="offer">
        <svg class="offer-icon" viewBox="0 0 30 30"><circle cx="15" cy="15" r="14" fill="none" stroke="#ee7d22" stroke-width="2"/><circle cx="15" cy="13" r="5" fill="#56647f"/><rect x="13" y="18" width="4" height="4" fill="#56647f"/></svg>
        <div><div class="offer-title">Wissen</div><div class="offer-text">aus jahrelanger Erfahrung.</div></div>
      </div>
      <div class="offer">
        <svg class="offer-icon" viewBox="0 0 30 30"><circle cx="15" cy="15" r="14" fill="none" stroke="#ee7d22" stroke-width="2"/><path d="M8 10h14v8h-8l-4 3v-3H8z" fill="#56647f"/></svg>
        <div><div class="offer-title">Persönliche Beratung</div><div class="offer-text">von der Idee bis zum Umzug.</div></div>
      </div>
      <div class="offer">
        <svg class="offer-icon" viewBox="0 0 30 30"><circle cx="15" cy="15" r="14" fill="none" stroke="#ee7d22" stroke-width="2"/><path d="M8 19a7 7 0 0114 0z" fill="#56647f"/></svg>
        <div>
          <div class="offer-title">Ausgebildete Fachkräfte</div><div class="offer-text">für:</div>
          <ul class="ticks">
            <li><svg viewBox="0 0 12 12"><circle cx="6" cy="6" r="5" fill="none" stroke="#ee7d22"/><path d="M3.5 6l2 2 3-3.5" fill="none" stroke="#ee7d22"/></svg>Montagearbeiten</li>
            <li><svg viewBox="0 0 12 12"><circle cx="6" cy="6" r="5" fill="none" stroke="#ee7d22"/><path d="M3.5 6l2 2 3-3.5" fill="none" stroke="#ee7d22"/></svg>Entrümpelung</li>
            <li><svg viewBox="0 0 12 12"><circle cx="6" cy="6" r="5" fill="none" stroke="#ee7d22"/><path d="M3.5 6l2 2 3-3.5" fill="none" stroke="#ee7d22"/></svg>Ein- und Auspackservice</li>
          </ul>
          <div class="offer-text" style="margin-top:6px">Das alles mit den modernsten und besten Werkzeugen.</div>
        </div>
      </div>
      <div class="offer">
        <svg class="offer-icon" viewBox="0 0 30 30"><circle cx="15" cy="15" r="14" fill="none" stroke="#ee7d22" stroke-width="2"/><path d="M9 14h3v8H9zM13 14l3-6c2 0 2 2 2 3v2h4v5l-2 4h-7z" fill="#56647f"/></svg>
        <div><div class="offer-title">Zuverlässigkeit</div><div class="offer-text">einen verlässlichen Umzugspartner.</div></div>
      </div>
    </div>
    <div class="contact">
      <div class="contact-label">Kontaktieren Sie uns:</div>
      <div class="contact-mail">info@pkv-transporte.example</div>
    </div>
  </article>

  <article class="panel">
    <div class="photo" style="height:300px">
      <div class="photo-fill" role="img" aria-label="Foto: lächelnder Umzugshelfer mit Kartons vor einem Wohnhaus" style="background:linear-gradient(135deg,#6b4a3a 0%,#c7b8a8 45%,#e6e2dc 100%)"></div>
      <svg class="photo-curve" viewBox="0 0 360 90" preserveAspectRatio="none"><path d="M0 90V70Q180 10 360 40V90z" fill="#fbfbfb"/><path d="M0 80Q10 50 40 48" fill="none" stroke="#ee7d22" stroke-width="6"/></svg>
      <div class="badge" style="left:40px;top:185px">
        <svg viewBox="0 0 24 24"><path d="M6 3l3 4-2 2c1 3 4 6 7 7l2-2 4 3-2 4C10 21 3 14 3 5z" fill="#fff"/></svg>
        <div class="badge-label">ANRUFEN</div>
        <div class="badge-number">0152 388<br>47261</div>
      </div>
    </div>
    <div class="copy" style="top:330px">
      <h2 class="heading">Ein- und Auspack<br>Service</h2>
      <p class="quiet">Haben Sie bei Ihrem Umzug Angst um Ihr Porzellan oder Geschirr?</p>
      <p class="quiet">Lassen Sie es doch einfach durch unsere Umzugsprofis einpacken und auspacken, damit auch nichts zu Bruch geht.</p>
      <div class="rule"></div>
      <h2 class="heading" style="margin-top:24px">Versicherung</h2>
      <p class="quiet">In alle unseren Angeboten ist selbstverständlich eine Transport- und Haftpflichtversicherung kostenlos enthalten.</p>
    </div>
  </article>

  <article class="panel">
    <div class="band-top"></div>
    <div class="copy" style="top:40px">
      <h2 class="heading" style="border-bottom:1px solid var(--orange);padding-bottom:10px">Privatumzüge</h2>
      <p class="lead">Sie freuen sich auf Ihre neuen vier Wände.</p>
      <p class="quiet">Vorher steht eine Menge Arbeit ins Haus: Ihr Umzug.</p>
      <p class="lead">Kein Problem, wir packen das für Sie an.</p>
      <p class="accent">PKV Transporte macht Ihren Möbeln Beine!</p>
      <p class="quiet">Unser Leistungsspektrum umfasst alle Dienstleistungen rund um Ihren Umzug aus einer Hand:</p>
      <p class="quiet">Wir packen ein und aus, demontieren und montieren sämtliche Möbel, leisten fachgerechte Schreiner-, Elektro- und Installationsarbeiten.</p>
      <p class="accent">Bei uns sind Sie auf der sicheren Seite!</p>
      <p class="quiet">Es wird alles zu einem Festpreis angeboten, nicht wie bei anderen Unternehmen, wo Sie am Ende noch mit Zusatzkosten rechnen müssen.</p>
      <p class="lead">In unserem Festpreis ist enthalten:</p>
      <p class="quiet">die Versicherung des Umzugsgutes, der/des Wohnung/Hauses, Schutzdecken für die Möbel sowie Gurte und Verpackungsmaterial, ausgenommen Umzugskartons.</p>
    </div>
  </article>
</section>

<section class="spread spread--outside">
  <article class="panel">
    <div class="band-top band-top--orange"></div>
    <div class="photo" style="top:8px;height:330px">
      <div class="photo-fill" role="img" aria-label="Foto: Umzugshelfer tragen Kartons aus einem Transporter" style="background:linear-gradient(160deg,#9fb6cf 0%,#c9b69a 50%,#3f5275 100%)"></div>
      <svg class="photo-curve" viewBox="0 0 360 90" preserveAspectRatio="none"><path d="M0 90V70Q180 10 360 40V90z" fill="#fbfbfb"/><path d="M0 80Q10 50 40 48" fill="none" stroke="#ee7d22" stroke-width="6"/></svg>
      <div class="badge" style="left:40px;top:215px">
        <svg viewBox="0 0 24 24"><path d="M6 3l3 4-2 2c1 3 4 6 7 7l2-2 4 3-2 4C10 21 3 14 3 5z" fill="#fff"/></svg>
        <div class="badge-label">ANRUFEN</div>
        <div class="badge-number">0152 388<br>47261</div>
      </div>
    </div>
    <div class="copy" style="top:400px">
      <h2 class="heading" style="font-size:28px;border-bottom:1px solid var(--orange);padding-bottom:10px">Über uns</h2>
      <p class="quiet" style="font-size:13px">PKV Transporte ist ein erfahrenes und kompetentes Umzugsunternehmen aus Talbrunn.</p>
      <p class="quiet" style="font-size:13px">Innerhalb der Umzugsbranche reduzieren wir uns nicht nur auf Privatumzüge, den unsere Palette reicht vom Firmenumzug, Entrümpelung und Ankauf von gebrauchte Büromöbeln so wie Personaldienstleistung in der Möbelbrache.</p>
    </div>
  </article>

  <article class="panel panel--navy">
    <div class="brand">PKV Transporte</div>
    <div class="address-list">
      <div class="address-item">
        <svg viewBox="0 0 26 26"><circle cx="13" cy="13" r="11" fill="none" stroke="#fff" stroke-width="1.5"/><path d="M13 19s-4-4-4-7a4 4 0 018 0c0 3-4 7-4 7z" fill="none" stroke="#fff" stroke-width="1.5"/></svg>
        <p>Lerchenfeldweg 27<br>74395 Lindenau am Kocher</p>
      </div>
      <div class="address-item">
        <svg viewBox="0 0 26 26"><circle cx="13" cy="13" r="11" fill="none" stroke="#fff" stroke-width="1.5"/><path d="M9 7l2 3-1 1c1 2 2 3 4 4l1-1 3 2-1 2c-5 0-10-5-10-10z" fill="#fff"/></svg>
        <p>0049 152 38847261</p>
      </div>
      <div class="address-item">
        <svg viewBox="0 0 26 26"><circle cx="13" cy="13" r="11" fill="none" stroke="#fff" stroke-width="1.5"/><rect x="7.5" y="9" width="11" height="8" fill="none" stroke="#fff" stroke-width="1.5"/><path d="M7.5 9l5.5 4.5L18.5 9" fill="none" stroke="#fff" stroke-width="1.5"/></svg>
        <p>info@pkv-transporte.example</p>
      </div>
      <div class="address-item">
        <p class="web-caps">WWW.PKV-TRANSPORTE.EXAMPLE</p>
      </div>
    </div>
  </article>

  <article class="panel">
    <div class="band-top band-top--orange"></div>
    <div class="brand cover-brand">PKV Transporte</div>
    <div class="photo" style="top:140px;height:400px">
      <div class="photo-fill" role="img" aria-label="Foto: zwei Umzugshelfer in Latzhosen mit Kartonstapel" style="background:linear-gradient(150deg,#d9c6ae 0%,#b89470 45%,#2f4577 100%)"></div>
      <svg class="photo-curve" viewBox="0 0 360 90" preserveAspectRatio="none"><path d="M0 90V70Q180 10 360 40V90z" fill="#fbfbfb"/><path d="M0 80Q10 50 40 48" fill="none" stroke="#ee7d22" stroke-width="6"/></svg>
      <div class="badge" style="left:40px;top:285px">
        <svg viewBox="0 0 24 24"><path d="M6 3l3 4-2 2c1 3 4 6 7 7l2-2 4 3-2 4C10 21 3 14 3 5z" fill="#fff"/></svg>
        <div class="badge-label">ANRUFEN</div>
        <div class="badge-number">0152 388<br>47261</div>
      </div>
    </div>
    <h1 class="heading cover-title">Ihr Profi für<br>Umzüge aller Art</h1>
    <div class="cover-web">www.pkv-transporte.example</div>
  </article>
</section>

</body>
</html>
```